Call Center In Need of Website Design

We are a call center that provides inbound and outbound calling & marketing services for eCommerce store. We would like to see a fun, creative, playful design that is simple.

Here are some sample design sites we like;
- https://www.velmorink.com/
- https://tonquel.io/
- https://www.brasklode.com/live-chat-software/
- https://www.quillarbe.com/

Here are some competitor sites;
- https://www.dorvenlinkage.com/
- https://www.helpwaldrix.com/

I have attached website content for your use.
Updates

Target Market(s)

eCommerce

Coding

Coded - Design and coding required

Number of Pages Required

5+ page

Font styles to use
Sans Serif

Colors

Designer to choose colors to be used in the design.

Requirements
Must have
• Must have designs for the following 5 separate pages;
• 1. Home (landing)
• - This will be were the design style really needs to show.
• - Just needs to touch on key services
• - CTA
• 2. About Us
• - Basic page for about me paragraph
• 3. Services
• - List of services with icons
• - Click on service type to expand details or hover over service icon to view popup bubble with details about that service
• 4. Pricing
• - Option to bundle 1(one) digital service plan and 1(one) call center service plan
• - Bundling adds 10% monthly discount to over all price
• - Customer does NOT have to bundle
• - FAQ
• 5. Contact Us
• - Include a capture form (name, company name, email, phone, message)
• - Contact info
• - Business hours
• When customer purchases their desired plan, then they are taken to a page where they must schedule a call with an account rep.
Nice to have
• home page animations
Should not have
• All information on Home/Landing page.

```html
<!DOCTYPE html>
<html lang="en">
<head>
<meta charset="utf-8">
<title>Lumora — Call Center &amp; Digital Support</title>
<link href="https://fonts.googleapis.com/css2?family=Poppins:wght@400;500;600;700&family=Open+Sans:wght@400;600&display=swap" rel="stylesheet">
<style>
  :root{
    --mint:#3edcb6;
    --mint-soft:#c9f5ea;
    --mint-pale:#eafbf6;
    --ink:#1f2a30;
    --text:#6b7378;
    --muted:#9aa2a6;
    --line:#e4e8ea;
    --dark:#1e2224;
    --darker:#151819;
    --white:#ffffff;
    --black:#0d0f10;
  }
  *{box-sizing:border-box;margin:0;padding:0}
  html,body{width:1200px;height:2264px;overflow:hidden}
  body{font-family:"Open Sans",Arial,sans-serif;color:var(--text);background:var(--white);position:relative}
  h1,h2,h3,h4{font-family:"Poppins",Arial,sans-serif;color:var(--ink);font-weight:500}
  .btn{display:inline-block;background:var(--black);color:var(--white);font-family:"Poppins",Arial,sans-serif;font-size:11px;font-weight:600;letter-spacing:.8px;text-transform:uppercase;padding:10px 22px;border-radius:20px;text-decoration:none}

  /* header */
  .site-header{position:absolute;top:0;left:0;width:1200px;height:64px;background:var(--white);display:flex;align-items:center;justify-content:space-between;padding:0 130px;box-shadow:0 1px 4px rgba(0,0,0,.06);z-index:5}
  .brand{display:flex;align-items:center;gap:10px;text-decoration:none}
  .brand-dot{width:26px;height:26px;border-radius:50%;background:var(--mint)}
  .brand-name{font-family:"Poppins",Arial,sans-serif;font-size:24px;font-weight:500;letter-spacing:4px;color:var(--ink);text-transform:uppercase}
  .main-nav{display:flex;gap:22px;align-items:center}
  .main-nav a{font-family:"Poppins",Arial,sans-serif;font-size:13px;color:#555;text-decoration:none}
  .main-nav a.active{color:var(--mint)}

  /* hero */
  .hero{position:absolute;top:64px;left:0;width:1200px;height:500px;background:linear-gradient(180deg,#bff3e4 0%,#eefcf8 70%,#ffffff 100%);text-align:center}
  .hero h1{font-size:34px;padding-top:104px}
  .hero p{width:520px;margin:16px auto 0;font-size:12px;line-height:1.75;color:#6b7a7a}
  .hero .btn{margin-top:30px}
  .hero-art{position:absolute;left:220px;top:300px;width:760px;height:170px;border-radius:14px;background:linear-gradient(90deg,#8fe8cf 0%,#f3d7c4 50%,#9fb7e8 100%);opacity:.75}
  .hero-cloud{position:absolute;left:0;bottom:-2px;width:1200px;height:70px}

  /* what we do */
  .what{position:absolute;top:580px;left:0;width:1200px;height:300px}
  .what-art{position:absolute;left:180px;top:30px;width:320px;height:230px;border-radius:16px;background:linear-gradient(135deg,#d6f6ee 0%,#e8ecf4 60%,#f6efe6 100%)}
  .what-copy{position:absolute;left:620px;top:80px;width:400px}
  .what-copy h2,.about-copy h2{font-size:22px;margin-bottom:12px}
  .what-copy p,.about-copy p{font-size:11.5px;line-height:1.75;margin-bottom:18px}

  /* about */
  .about{position:absolute;top:900px;left:0;width:1200px;height:460px;background:#fbfbfb;border-top:1px solid var(--line)}
  .about-copy{position:absolute;left:130px;top:80px;width:440px}
  .about-art{position:absolute;left:690px;top:90px;width:330px;height:250px;border-radius:18px;background:linear-gradient(135deg,#e4ecf9 0%,#dff7f0 55%,#fbe7dd 100%)}

  /* subscribe */
  .subscribe{position:absolute;top:1360px;left:0;width:1200px;height:440px;background:linear-gradient(180deg,#ffffff 0%,#d9f8ef 55%,#9eeed7 100%);text-align:center}
  .sub-cloud{position:absolute;top:0;left:0;width:1200px;height:90px}
  .subscribe h2{font-size:22px;padding-top:126px}
  .sub-form{width:440px;margin:28px auto 0;display:flex;flex-direction:column;gap:10px}
  .sub-form .field{height:34px;border-radius:17px;background:var(--white);border:1px solid #d7e4e0;text-align:left;padding:0 18px;font-size:11px;color:var(--muted);line-height:32px}
  .sub-form .submit{height:32px;border-radius:16px;background:var(--black);color:var(--white);font-family:"Poppins",Arial,sans-serif;font-size:11px;font-weight:600;letter-spacing:1px;line-height:32px;text-transform:uppercase}
  .sub-note{margin-top:16px;font-size:10px;color:#7d8a86}

  /* footer */
  .site-footer{position:absolute;top:1800px;left:0;width:1200px;height:440px;background:var(--dark);display:flex;gap:0;padding:70px 130px 0}
  .foot-col{width:235px}
  .foot-col h4{color:var(--mint);font-size:14px;font-weight:600;margin-bottom:16px}
  .foot-col ul{list-style:none}
  .foot-col li{font-size:10.5px;color:#c7cbcd;line-height:2;padding-left:12px;position:relative}
  .foot-col li::before{content:"";position:absolute;left:0;top:10px;width:4px;height:4px;border-radius:50%;background:var(--mint)}
  .foot-col address{font-style:normal;font-size:10.5px;color:#c7cbcd;line-height:2}
  .foot-bottom{position:absolute;top:2240px;left:0;width:1200px;height:24px;background:var(--darker);padding:0 130px;font-size:9px;color:#8b9194;line-height:24px}
</style>
</head>
<body>

<header class="site-header">
  <a class="brand" href="#"><span class="brand-dot"></span><span class="brand-name">Lumora</span></a>
  <nav class="main-nav">
    <a class="active" href="#">Home</a>
    <a href="#">About Us</a>
    <a href="#">What We Do</a>
    <a href="#">Pricing</a>
    <a href="#">FAQs</a>
    <a href="#">Contact</a>
    <svg width="14" height="14" viewBox="0 0 14 14" aria-label="Search"><circle cx="6" cy="6" r="4.5" fill="none" stroke="#777" stroke-width="1.5"/><line x1="9.4" y1="9.4" x2="13" y2="13" stroke="#777" stroke-width="1.5"/></svg>
  </nav>
</header>

<section class="hero">
  <h1>Lumora</h1>
  <p>Lumora is an omnichannel provider for customer and outbound call support. We primarily assist with eCommerce companies around the world. Our mission is to grow the operations and functionality of your store through reliable, friendly customer support.</p>
  <a class="btn" href="#">Get Started</a>
  <div class="hero-art" role="img" aria-label="Illustration of two support agents working at desks with laptops, a plant, a lamp and a wall clock"></div>
  <svg class="hero-cloud" viewBox="0 0 1200 70" preserveAspectRatio="none" aria-hidden="true">
    <path d="M0 40 C60 10 120 20 170 38 C220 12 300 14 340 40 C400 20 470 22 520 44 C580 18 660 18 700 42 C760 20 830 20 880 44 C930 18 1010 16 1050 40 C1100 20 1160 24 1200 36 L1200 70 L0 70 Z" fill="#ffffff"/>
  </svg>
</section>

<section class="what">
  <div class="what-art" role="img" aria-label="Illustration of a support team connected by chat, phone and email icons"></div>
  <div class="what-copy">
    <h2>What We Do</h2>
    <p>Lumora is your personal customer service and product research team. We look at eCommerce, like we love taking business owners' success and share it with you. Lumora handles your customers while you focus on growing your business.</p>
    <a class="btn" href="#">Learn More</a>
  </div>
</section>

<section class="about">
  <div class="about-copy">
    <h2>About Us</h2>
    <p>Lumora is an omnichannel provider for customer and outbound call support. We primarily work with eCommerce companies around the world. Our mission is to aid in the core operations and functionality of consumer-focused online businesses.</p>
    <p>Lumora originally started out as a general virtual call center support company. Based in California, the founder quickly realized that there was a lack of support for eCommerce owners that were just getting started. In 2018, Lumora shifted its gears to offer professional grade call center support at a price that even new start-ups could afford.</p>
    <a class="btn" href="#">Learn More</a>
  </div>
  <div class="about-art" role="img" aria-label="Illustration of customer support agents with headsets around a central laptop"></div>
</section>

<section class="subscribe">
  <svg class="sub-cloud" viewBox="0 0 1200 90" preserveAspectRatio="none" aria-hidden="true">
    <path d="M0 0 L1200 0 L1200 46 C1150 70 1090 66 1050 50 C1000 76 930 74 890 52 C840 78 760 76 720 54 C670 80 590 78 550 54 C500 80 420 76 380 52 C330 76 250 74 210 50 C160 74 80 70 40 50 C25 56 10 56 0 54 Z" fill="#ffffff"/>
  </svg>
  <h2>Subscribe for a Free Trial!</h2>
  <div class="sub-form">
    <div class="field">Name</div>
    <div class="field">Email</div>
    <div class="submit">Submit</div>
  </div>
  <p class="sub-note">We promise we won't spam you</p>
</section>

<footer class="site-footer">
  <div class="foot-col">
    <h4>Digital Services</h4>
    <ul>
      <li>Email Support</li>
      <li>Live Chat Support</li>
      <li>Product Reviews</li>
      <li>Product Entry</li>
      <li>Price Monitoring</li>
      <li>Product Photo &amp; Data Editing</li>
    </ul>
  </div>
  <div class="foot-col">
    <h4>Call Center Services</h4>
    <ul>
      <li>Inbound Calls</li>
      <li>Outbound Calls</li>
      <li>Follow-Up Services</li>
      <li>Customer Handling</li>
      <li>Order Via Phone / Order Taking</li>
      <li>Order Return Processing</li>
      <li>Feedback &amp; Survey Calls</li>
      <li>Message Taking Service</li>
      <li>24/7 Inquiries &amp; Reporting</li>
      <li>Upsell &amp; Cross-Selling</li>
      <li>Commission &amp; Pay Delivery</li>
      <li>Affiliate Program</li>
    </ul>
  </div>
  <div class="foot-col">
    <h4>Quick Links</h4>
    <ul>
      <li>Home</li>
      <li>About Us</li>
      <li>What We Do</li>
      <li>Pricing</li>
      <li>FAQs</li>
      <li>Contact</li>
    </ul>
  </div>
  <div class="foot-col">
    <h4>Contact Us</h4>
    <address>Lumora Inc.<br>755 Fairview Drive<br>Eastlake, CA 92915<br>(555) 014-2277</address>
  </div>
</footer>
<div class="foot-bottom">© 2019 Lumora Inc. All rights reserved.</div>

</body>
</html>
```